Dorvanski Law Rebrand

I am recreating my law firm website. I got a new logo and would like to recreate the website to match the new logo. the website is dorvanskilaw.com

```html
<!DOCTYPE html>
<html lang="en">
<head>
<meta charset="utf-8">
<title>Dorvanski Law, PLLC</title>
<link href="https://fonts.googleapis.com/css2?family=Catamaran:wght@600;700;800&family=Roboto:wght@400;500&family=Open+Sans:wght@400;600&display=swap" rel="stylesheet">
<style>
:root{
  --navy:#0b4f94;
  --navy-dark:#0a3f78;
  --steel:#9fadc6;
  --steel-light:#c9d3e3;
  --ink:#111111;
  --text:#444a52;
  --white:#ffffff;
  --black:#000000;
}
*{box-sizing:border-box;margin:0;padding:0}
html,body{width:1200px;height:3439px;overflow:hidden;background:var(--white)}
body{position:relative;font-family:"Roboto",sans-serif;color:var(--text)}
.abs{position:absolute}
.heading{font-family:"Catamaran",sans-serif;font-weight:800;text-transform:uppercase}

/* header */
.topbar{left:330px;top:0;width:870px;height:60px;background:var(--steel);clip-path:polygon(0 0,100% 0,100% 100%,42px 100%);color:var(--white);font-family:"Catamaran",sans-serif;font-weight:600;font-size:17px}
.topbar .addr{left:80px;top:19px;display:flex;gap:6px;align-items:center}
.topbar .sep{left:524px;top:20px;width:2px;height:18px;background:var(--white)}
.topbar .phone{left:570px;top:19px;display:flex;gap:6px;align-items:center}
.brand{left:112px;top:84px;font-family:"Catamaran",sans-serif;font-weight:700;font-size:24px;letter-spacing:3px;color:var(--navy);display:flex;align-items:center;gap:10px}
.brand .dot{width:16px;height:16px;background:var(--navy)}
.nav{left:384px;top:96px;display:flex;gap:31px;font-family:"Catamaran",sans-serif;font-weight:700;font-size:16px;color:var(--ink)}
.nav .active{color:var(--navy)}
.btn{display:inline-flex;align-items:center;gap:8px;background:var(--navy);color:var(--white);font-family:"Catamaran",sans-serif;font-weight:800;font-size:16px;text-transform:uppercase;height:48px;padding:0 36px 0 28px;clip-path:polygon(0 0,90% 0,100% 100%,0 100%)}
.btn svg{width:18px;height:10px}

/* hero */
.hero{left:0;top:151px;width:1200px;height:647px;background:linear-gradient(135deg,#3f6d9e 0%,#5b86b5 45%,#3d6a9a 75%,#2f5c8f 100%)}
.hero-title{left:0;top:300px;width:1200px;text-align:center;color:var(--white);font-size:41px;line-height:56px}
.hero-copy{left:255px;top:444px;width:690px;text-align:center;color:var(--white);font-size:15.5px;line-height:26px}
.hero-copy p+p{margin-top:26px}
.hero .btn{}
.notch{left:520px;top:767px;width:160px;height:40px;background:var(--white);clip-path:polygon(0 100%,50% 0,100% 100%)}

/* welcome */
.welcome-title{left:114px;top:948px;font-size:41px;line-height:56px;color:var(--ink)}
.welcome-title span{color:var(--navy)}
.rule{left:0;top:1073px;width:237px;height:2px;background:var(--steel)}
.welcome-copy{left:114px;top:1101px;width:424px;font-size:14px;line-height:22.6px;text-align:justify}
.welcome-copy p+p{margin-top:22px}
.portrait{left:575px;top:958px;width:613px;height:625px;background:linear-gradient(180deg,#dfe6ef 0%,#c8d4e3 50%,#2b3550 100%)}
.accent-line{left:1140px;top:1000px;width:2px;height:135px;background:var(--navy)}

/* practice */
.practice-bg{left:0;top:1583px;width:1200px;height:375px;background:linear-gradient(135deg,#1e5894,#2d6aa6 50%,#0f4f92)}
.practice-bg-low{left:0;top:1958px;width:658px;height:251px;background:#155b9c}
.practice-title{left:0;top:1642px;width:1200px;text-align:center;color:var(--white);font-size:44px}
.practice-rule{left:556px;top:1716px;width:88px;height:4px;background:var(--steel)}
.pcard{left:113px;top:1769px;width:974px;height:356px;background:linear-gradient(120deg,#8f9fbf,#a8b6d0 60%,#9caccb)}
.picon{left:42px;top:28px;width:82px;height:82px;border-radius:50%;border:2px dashed var(--white);display:flex;align-items:center;justify-content:center}
.picon div{width:64px;height:64px;border-radius:50%;background:var(--navy)}
.pcard h3{left:42px;top:130px;font-family:"Open Sans",sans-serif;font-weight:600;font-size:27px;color:var(--white)}
.pcard .pdesc{left:45px;top:188px;width:430px;font-family:"Open Sans",sans-serif;font-size:12.5px;line-height:24.5px;color:var(--white)}
.pcard .learn{left:47px;top:279px;font-family:"Open Sans",sans-serif;font-size:12.5px;color:var(--white);display:flex;gap:8px;align-items:center}
.plist{left:645px;top:44px;width:285px;font-family:"Open Sans",sans-serif;font-weight:600;font-size:16px;color:var(--white)}
.plist li{list-style:none;height:59px;padding:16px 15px;border-bottom:1px solid rgba(255,255,255,.6)}
.plist li.on{background:var(--white);color:var(--navy);height:51px;padding:13px 15px;border:2px solid var(--navy);margin-bottom:2px}
.plist li:last-child{border-bottom:none}

/* news */
.news-title{left:0;top:2300px;width:1200px;text-align:center;font-size:46px;color:var(--ink)}
.news-rule{left:556px;top:2360px;width:88px;height:3px;background:var(--steel)}
.card{top:2396px;width:324px;height:414px;background:var(--white);border-radius:18px;box-shadow:0 2px 12px rgba(0,0,0,.08)}
.card .ph{left:9px;top:10px;width:307px;height:206px;border-radius:16px}
.card .date{left:44px;top:232px;font-size:15px;color:#333}
.card h4{left:44px;top:264px;width:260px;font-family:"Roboto",sans-serif;font-weight:500;font-size:20px;line-height:28px;color:var(--ink)}
.card .ex{left:44px;top:334px;width:256px;font-size:13.5px;line-height:20px;color:#777}
.arrow-c{top:2568px;width:26px;height:26px}

/* footer */
.footer{left:0;top:2993px;width:1200px;height:446px;background:var(--black);color:var(--white)}
.fbrand{left:127px;top:188px;font-family:"Catamaran",sans-serif;font-weight:700;font-size:24px;letter-spacing:3px;color:var(--navy);display:flex;align-items:center;gap:10px}
.fbrand .dot{width:16px;height:16px;background:var(--navy)}
.social{left:191px;top:258px;display:flex;gap:11px}
.social span{width:29px;height:29px;border-radius:50%;background:var(--white)}
.social span.mid{background:#9aa8c4}
.fcol h5{font-family:"Roboto",sans-serif;font-weight:500;font-size:21px;text-transform:uppercase}
.fcol h5::after{content:"";display:block;width:34px;height:2px;background:var(--navy);margin-top:12px}
.fcol ul{list-style:none;margin-top:16px;font-size:15px}
.fcol li{display:flex;gap:16px;margin-bottom:11px;line-height:21px}
.fcol li::before{content:"»";font-size:15px}
.news-form{left:837px;top:225px;width:253px;height:45px;display:flex}
.news-form .field{flex:1;background:#9aa8c4;font-size:14px;color:var(--white);padding:13px 13px}
.news-form .send{width:49px;background:var(--navy);display:flex;align-items:center;justify-content:center}
.frule{left:126px;top:350px;width:978px;height:1px;background:#555}
.copy{left:0;top:392px;width:1200px;text-align:center;font-family:"Catamaran",sans-serif;font-size:15.5px}
</style>
</head>
<body>

<header>
  <div class="abs topbar">
    <div class="abs addr"><svg width="11" height="14" viewBox="0 0 11 14"><path d="M5.5 0A5.5 5.5 0 0 0 0 5.5C0 9.6 5.5 14 5.5 14S11 9.6 11 5.5A5.5 5.5 0 0 0 5.5 0zm0 7.6a2.1 2.1 0 1 1 0-4.2 2.1 2.1 0 0 1 0 4.2z" fill="#fff"/></svg>245 N. Harlow Avenue Suite B Kingsley, Texas 77390</div>
    <div class="abs sep"></div>
    <div class="abs phone"><svg width="13" height="13" viewBox="0 0 24 24"><path d="M6.6 10.8a15.1 15.1 0 0 0 6.6 6.6l2.2-2.2c.3-.3.7-.4 1-.2 1.1.4 2.3.6 3.6.6.6 0 1 .4 1 1V20c0 .6-.4 1-1 1A17 17 0 0 1 3 4c0-.6.4-1 1-1h3.5c.6 0 1 .4 1 1 0 1.3.2 2.5.6 3.6.1.3 0 .7-.2 1z" fill="#fff"/></svg>+1 281-555-0142</div>
  </div>
  <div class="abs brand"><span class="dot"></span>DORVANSKI LAW</div>
  <nav class="abs nav"><span class="active">HOME</span><span>PRACTICES AREAS</span><span>ABOUT ME</span><span>BLOG</span></nav>
  <a class="abs btn" style="left:800px;top:83px;height:47px">Schedule a Consultation <svg viewBox="0 0 18 10"><path d="M0 5h15M11 1l4 4-4 4" stroke="#fff" stroke-width="2" fill="none"/></svg></a>
</header>

<section class="abs hero" role="img" aria-label="Blue-tinted photo of glass office towers seen from below"></section>
<h1 class="abs heading hero-title">Personal Legal Solutions<br>in Life's Most Difficult Moments</h1>
<div class="abs hero-copy">
  <p>Helping clients navigate probate, guardianships, estate planning, and other civil disputes by providing personal attention to each client; knowing their objectives; understanding their needs; and then thinking creatively to achieve those goals.</p>
  <p>Every case is different and each client is unique - I believe that when an attorney approaches them as such, the outcomes can be better than ever anticipated.</p>
</div>
<a class="abs btn" style="left:452px;top:631px">Schedule a Consultation <svg viewBox="0 0 18 10"><path d="M0 5h15M11 1l4 4-4 4" stroke="#fff" stroke-width="2" fill="none"/></svg></a>
<div class="abs notch"></div>

<section>
  <h2 class="abs heading welcome-title">Welcome to<br><span>Dorvanski Law, PLLC</span></h2>
  <div class="abs rule"></div>
  <div class="abs welcome-copy">
    <p>It is my honor to provide quality legal services at a reasonable price to clients that I enjoy working with and for. I am grateful for all my clients and the trust they place in me to represent them.</p>
    <p>My practice focuses on Probate, Adult Guardianships, and Trust Administration and Litigation. I also represent clients in other general civil litigation matters. Finally, I handle estate planning for families of modest means.</p>
    <p>As your attorney, I would educate you about the law as it pertains to your situation, guide you through your options, and then help you to achieve your desired objectives from those options.</p>
    <p>Schedule your consultation today.</p>
  </div>
  <a class="abs btn" style="left:113px;top:1456px">Schedule a Consultation <svg viewBox="0 0 18 10"><path d="M0 5h15M11 1l4 4-4 4" stroke="#fff" stroke-width="2" fill="none"/></svg></a>
  <div class="abs portrait" role="img" aria-label="Portrait photo of the attorney in a navy suit and red tie"></div>
  <div class="abs accent-line"></div>
</section>

<section>
  <div class="abs practice-bg" role="img" aria-label="Blue-tinted photo of a law library and courtroom"></div>
  <div class="abs practice-bg-low"></div>
  <h2 class="abs heading practice-title">Practice Area</h2>
  <div class="abs practice-rule"></div>
  <div class="abs pcard">
    <div class="abs picon"><div></div></div>
    <h3 class="abs">Probate and Trusts</h3>
    <p class="abs pdesc">Guiding clients through the legal process of administering a deceased person's estate, ensuring that assets are distributed according to their wishes while addressing any legal complexities that may arise.</p>
    <div class="abs learn">LEARN MORE <svg width="13" height="13" viewBox="0 0 13 13"><circle cx="6.5" cy="6.5" r="6.5" fill="#fff"/><path d="M4 6.5h5M7 4l2.5 2.5L7 9" stroke="#9fadc6" stroke-width="1.5" fill="none"/></svg></div>
    <ul class="abs plist">
      <li class="on">Probate and Trusts</li>
      <li>Estate Planning</li>
      <li>Adult Guardianships</li>
      <li>Civil Litigation</li>
      <li>Individuals</li>
    </ul>
  </div>
</section>

<section>
  <h2 class="abs heading news-title">News &amp; Articles</h2>
  <div class="abs news-rule"></div>
  <svg class="abs arrow-c" style="left:54px" viewBox="0 0 26 26"><circle cx="13" cy="13" r="11.5" fill="none" stroke="#111" stroke-width="1.8"/><path d="M15 8l-5 5 5 5" fill="none" stroke="#111" stroke-width="1.8"/></svg>
  <svg class="abs arrow-c" style="left:1115px" viewBox="0 0 26 26"><circle cx="13" cy="13" r="11.5" fill="none" stroke="#111" stroke-width="1.8"/><path d="M11 8l5 5-5 5" fill="none" stroke="#111" stroke-width="1.8"/></svg>
  <article class="abs card" style="left:97px">
    <div class="abs ph" role="img" aria-label="Photo of a woman with glasses in a library" style="background:linear-gradient(135deg,#5a4634,#8c7458 60%,#3e3326)"></div>
    <div class="abs date">Oct 2025</div>
    <h4 class="abs">Trusts vs. Wills</h4>
    <p class="abs ex">Whether you need assistance with a dispute in relation to financial services, fraud, debt recovery, insurance, or</p>
  </article>
  <article class="abs card" style="left:437px">
    <div class="abs ph" role="img" aria-label="Photo of a meeting room with a city view" style="background:linear-gradient(135deg,#1d3550,#4f86b8 55%,#a9cbe6)"></div>
    <div class="abs date">Oct 2025</div>
    <h4 class="abs">Why probate is needed,… sometimes</h4>
    <p class="abs ex">From terms and conditions to ensuring client contracts are airtight, we're on top of the A to Z of commercial law.</p>
  </article>
  <article class="abs card" style="left:776px">
    <div class="abs ph" role="img" aria-label="Photo of a handshake over a signed document" style="background:linear-gradient(135deg,#2a2f3a,#8a7866 55%,#d9d3cc)"></div>
    <div class="abs date">Oct 2025</div>
    <h4 class="abs">Estate Planning Essentials</h4>
    <p class="abs ex">Whether you need assistance with a dispute in relation to financial services, fraud, debt recovery, insurance, or</p>
  </article>
  <a class="abs btn" style="left:508px;top:2868px;padding:0 40px 0 36px">View More <svg viewBox="0 0 18 10"><path d="M0 5h15M11 1l4 4-4 4" stroke="#fff" stroke-width="2" fill="none"/></svg></a>
</section>

<footer class="abs footer">
  <div class="abs fbrand"><span class="dot"></span>DORVANSKI LAW</div>
  <div class="abs social"><span></span><span class="mid"></span><span></span></div>
  <div class="abs fcol" style="left:424px;top:100px">
    <h5>Locations</h5>
    <ul><li>Home</li><li>About Us</li><li>Practice Area</li><li>Blog</li><li>Contact</li></ul>
  </div>
  <div class="abs fcol" style="left:605px;top:100px;width:200px">
    <h5>Contact</h5>
    <ul><li>245 N. Harlow Avenue Suite B Kingsley, Texas 77390</li><li>(281) 555-0142</li><li style="margin-top:12px">Mon - Fri&nbsp; 8AM - 5PM</li></ul>
  </div>
  <div class="abs fcol" style="left:832px;top:100px;width:270px">
    <h5>Newsletter Sign Up</h5>
    <p style="margin:18px 0 0 6px;font-size:15px;line-height:21px">We Will Notify You Of Any Important News</p>
  </div>
  <div class="abs news-form"><div class="field">Email Address</div><div class="send"><svg width="16" height="16" viewBox="0 0 16 16"><path d="M15 1L1 7l5 2 2 5z" fill="#fff"/></svg></div></div>
  <div class="abs frule"></div>
  <div class="abs copy">© 2025 Dorvanski Law, PLLC | All Rights Reserved</div>
</footer>

</body>
</html>
```